Forest Consultant/Timber Buyer needs a clean business card

We are a forestry consulting and timber buying company. We meet with private landowners and assist them with timber management and timber harvesting. We would like a professional business card, please no clip art. logo is blue and white but would like to see a gray,silver, or some other color incorporated. Would like basic contact info. Would like to the layout to be creative and sleek but masculine.

Target Market(s)

private landowners

Industry/Entity Type

Business

Contact Information for Business Card

name,position, cell number, office number, email, website. This might be to cluttered. Basic contact info is what we are looking for.

Contact info can all be on one side with logo on the other.

Font styles to use
Serif
Sans Serif

Colors
0255a3
ffffff
aaaaaa

Requirements
Must have
• We just want it professional.
Nice to have
• Creative layout.
Should not have
• please no clip art of log trucks etc.

```html
<!DOCTYPE html>
<html lang="en">
<head>
<meta charset="utf-8">
<title>Ridgeline Land &amp; Timber – Business Card</title>
<link rel="stylesheet" href="https://fonts.googleapis.com/css2?family=Lato:wght@400;700;900&display=swap">
<style>
  :root {
    --brand-blue: #0255a3;
    --ink-gray: #444444;
    --silver: #aaaaaa;
    --card-white: #ffffff;
    --card-shade: #eef0f3;
    --faint-blue: rgba(2, 85, 163, 0.10);
    --stage: #2a2a2a;
  }
  * { box-sizing: border-box; margin: 0; padding: 0; }
  html, body {
    width: 1200px;
    height: 873px;
    overflow: hidden;
    background: var(--stage);
    font-family: "Lato", sans-serif;
  }
  .sheet {
    width: 1200px;
    height: 873px;
    display: flex;
    align-items: center;
    justify-content: center;
    gap: 40px;
  }
  .card {
    position: relative;
    width: 540px;
    height: 309px;
    background: linear-gradient(135deg, var(--card-white) 0%, var(--card-shade) 100%);
    overflow: hidden;
  }

  /* Front */
  .card-front .backdrop {
    position: absolute;
    right: -40px;
    top: -60px;
    width: 320px;
    height: 320px;
    border-radius: 50%;
    background: var(--faint-blue);
  }
  .brand {
    display: flex;
    align-items: center;
    gap: 14px;
    color: var(--brand-blue);
    font-weight: 900;
    text-transform: uppercase;
  }
  .brand-dot {
    border-radius: 50%;
    background: var(--brand-blue);
    flex: none;
  }
  .card-front .brand {
    position: absolute;
    left: 60px;
    top: 120px;
    font-size: 30px;
    letter-spacing: 1px;
    line-height: 1.05;
  }
  .card-front .brand-dot { width: 44px; height: 44px; }

  /* Back */
  .card-back .backdrop {
    position: absolute;
    left: -70px;
    top: 40px;
    width: 330px;
    height: 330px;
    border-radius: 50%;
    background: var(--faint-blue);
  }
  .card-back .brand {
    position: absolute;
    right: 30px;
    top: 26px;
    font-size: 17px;
    letter-spacing: 0.5px;
    line-height: 1.05;
    gap: 10px;
  }
  .card-back .brand-dot { width: 26px; height: 26px; }
  .person {
    position: absolute;
    left: 70px;
    top: 196px;
  }
  .person-name {
    color: var(--brand-blue);
    font-weight: 700;
    font-size: 20px;
  }
  .person-role {
    color: var(--ink-gray);
    font-size: 15px;
    margin-top: 2px;
    padding-left: 40px;
  }
  .contact-list {
    position: absolute;
    left: 320px;
    top: 112px;
    list-style: none;
  }
  .contact-list li {
    display: flex;
    align-items: center;
    gap: 12px;
    color: var(--ink-gray);
    font-size: 14px;
    height: 28px;
  }
  .contact-list svg { width: 16px; height: 16px; flex: none; }
  .website {
    position: absolute;
    left: 320px;
    top: 230px;
    color: var(--brand-blue);
    font-weight: 700;
    font-size: 16px;
  }
  .accent-bar {
    position: absolute;
    left: 0;
    bottom: 0;
    width: 100%;
    height: 6px;
    background: var(--silver);
  }
</style>
</head>
<body>
<main class="sheet">
  <section class="card card-front" aria-label="Card front">
    <div class="backdrop"></div>
    <div class="brand">
      <span class="brand-dot"></span>
      <span>Ridgeline<br>Land &amp; Timber</span>
    </div>
  </section>

  <section class="card card-back" aria-label="Card back">
    <div class="backdrop"></div>
    <div class="brand">
      <span class="brand-dot"></span>
      <span>Ridgeline<br>Land &amp; Timber</span>
    </div>

    <ul class="contact-list">
      <li>
        <svg viewBox="0 0 16 16" aria-hidden="true"><rect x="3.5" y="1" width="9" height="14" rx="1.5" fill="none" stroke="#0255a3" stroke-width="1.5"/><circle cx="8" cy="12.5" r="0.9" fill="#0255a3"/></svg>
        <span>612.555.0148</span>
      </li>
      <li>
        <svg viewBox="0 0 16 16" aria-hidden="true"><rect x="4" y="1" width="8" height="4" fill="#0255a3"/><rect x="1" y="5" width="14" height="7" rx="1" fill="#0255a3"/><rect x="4" y="10" width="8" height="5" fill="#ffffff" stroke="#0255a3" stroke-width="1.2"/></svg>
        <span>612.555.0193</span>
      </li>
      <li>
        <svg viewBox="0 0 16 16" aria-hidden="true"><rect x="1" y="3" width="14" height="10" fill="#0255a3"/><path d="M1 3 L8 9 L15 3" fill="none" stroke="#ffffff" stroke-width="1.2"/></svg>
        <span>morgan@ridgelinetimber.com</span>
      </li>
    </ul>
    <div class="website">www.ridgelinetimber.com</div>

    <div class="person">
      <div class="person-name">Morgan Hale</div>
      <div class="person-role">Founder / Owner</div>
    </div>
  </section>
</main>
</body>
</html>
```